Parcelnook.com.au Front page Re-Design

We need a front page redesign for the website parcelnook.com.au,
The site needs to keep a number of products products highlighted on the front page. Same buttons but navigation could be different and we still need some text for SEO.
What we do not currently like:
1. The big banners.
2. The use of too much orange especially the 50% orange borders.
3. the fact that products cannot be seen straight away when logged-in.
4. The fact that it is hard to convert to tablet friendly
5. The fact that it's not a modern design.

What we think we want:

1. Maybe more use of 1 colour (purple or orange) with the other a secondary highlight colour.
2. A more modern look
3. The wow factor

Look at parcelnook.com.au take the elements that you need and design.
Updates

Project Deadline Extended
Reason: Designs are getting better. liking the designs that don't look like the usual e-commerce templates out there.

Hello,

We are making decisions next Monday. Sorry for the delay but there has been a lot of holidays in Australia and decision makers away.

Industry/Entity Type

Seo

Colors
6b449b
f78f20
ffffff

```html
<!DOCTYPE html>
<html lang="en">
<head>
<meta charset="utf-8">
<title>Parcelnook.com.au – Gift Baskets &amp; Hampers</title>
<link href="https://fonts.googleapis.com/css2?family=Open+Sans:wght@400;600&family=Quicksand:wght@300;400&display=swap" rel="stylesheet">
<style>
:root{
  --purple:#6b449b;
  --purple-dark:#553580;
  --orange:#f78f20;
  --white:#ffffff;
  --text:#444444;
  --muted:#888888;
  --line:#e2e2e2;
  --footer-bg:#f1f1f1;
  --bar-bg:#4a4a4a;
  --link-blue:#2a86c8;
}
*{box-sizing:border-box;margin:0;padding:0}
html,body{width:757px;height:1200px;overflow:hidden;background:var(--white)}
body{position:relative;font-family:"Open Sans",Arial,sans-serif;color:var(--text)}
.abs{position:absolute}

/* header */
.brand{left:56px;top:28px;display:flex;align-items:center;gap:8px}
.brand-mark{width:26px;height:26px;background:var(--orange)}
.brand-name{font-size:19px;font-weight:600;color:var(--purple)}
.brand-tag{left:58px;top:64px;font-size:8px;color:var(--purple)}
.locale{right:57px;top:23px;font-size:7px;color:var(--text);word-spacing:6px}
.account{right:57px;top:37px;font-size:7px;color:var(--text)}
.account span{margin-left:10px}
.account span::before{content:"";display:inline-block;width:5px;height:5px;background:#555;margin-right:4px;border-radius:1px}
.checkout{left:543px;top:54px;width:55px;height:23px;background:var(--orange);color:var(--white);font-size:7px;display:flex;align-items:center;justify-content:center;border-radius:2px}
.cart{left:605px;top:54px;width:96px;height:23px;border:1px solid #ccc;border-radius:2px;font-size:7px;color:#e4384c;display:flex;align-items:center;padding-left:7px;gap:5px}
.cart svg{flex:none}

/* nav */
.nav{left:56px;top:97px;width:645px;height:27px;background:var(--purple);border-radius:2px;display:flex;align-items:center;padding-left:8px;gap:0}
.nav a{color:var(--white);font-size:8px;text-decoration:none;padding:0 12px;letter-spacing:.2px}
.nav a.drop::after{content:"⌄";margin-left:4px}

/* banner */
.banner{left:56px;top:138px;width:645px;height:180px;border:1px solid var(--line);overflow:hidden;background:linear-gradient(90deg,#ffffff 0%,#ffffff 42%,#dfeec6 62%,#9cc85a 80%,#f2c23a 100%)}
.banner-kicker{left:16px;top:26px;font-family:"Quicksand",sans-serif;font-size:13px;color:var(--purple)}
.banner-title{left:16px;top:50px;font-family:"Quicksand",sans-serif;font-weight:300;font-size:40px;line-height:41px;color:var(--purple);letter-spacing:2px}
.dots{left:21px;top:150px;display:flex;gap:4px}
.dots i{width:5px;height:5px;border-radius:50%;background:var(--orange)}
.dots i:first-child{width:7px;height:7px;margin-top:-1px}

/* sidebar */
.side-head{left:56px;width:139px;height:26px;background:var(--purple);color:var(--white);font-size:10px;display:flex;align-items:center;padding-left:8px;border-radius:2px}
.side-list{left:62px;width:131px;list-style:none}
.side-list li{font-size:6.5px;height:17px;display:flex;align-items:center;border-bottom:1px solid #eee;color:#333}
.side-list li::before{content:"";width:7px;height:7px;border-radius:50%;background:var(--orange);margin-right:6px;flex:none}
.side-list li.on{color:var(--orange)}

/* products */
.prod-head{left:228px;top:342px;width:473px;height:25px;background:var(--purple);color:var(--white);font-size:10px;display:flex;align-items:center;padding-left:9px;border-radius:2px}
.card{width:100px;height:144px;border:1px solid var(--line);overflow:hidden}
.card .photo{position:absolute;left:12px;top:10px;width:76px;height:84px;border-radius:6px}
.card .ribbon{position:absolute;left:0;top:0}
.card .name{position:absolute;left:8px;top:98px;font-size:7px;line-height:9px;color:#555;width:88px}
.card .price{position:absolute;left:8px;top:122px;font-size:9px;color:var(--muted)}
.card .buy{position:absolute;right:5px;top:120px;width:42px;height:12px;background:var(--orange);color:var(--white);font-size:7px;display:flex;align-items:center;justify-content:center;border-radius:1px}

/* seo */
.seo{left:56px;top:885px;width:645px;height:111px;border:1px solid var(--line);display:flex}
.seo-col{flex:1;padding:15px 20px}
.seo-col + .seo-col{border-left:1px solid var(--line)}
.seo h2{font-weight:400;font-size:11px;color:#444;margin-bottom:8px}
.seo p{font-size:8px;line-height:13.5px;color:var(--muted)}

/* footer */
.footer{left:56px;top:1018px;width:645px;height:154px;background:var(--footer-bg)}
.f-title{font-size:9.5px;color:var(--link-blue)}
.f-list{font-size:6.5px;line-height:13px;color:#444;list-style:none}
.f-input{width:106px;height:15px;border:1px solid #ccc;border-radius:2px;background:var(--white);font-size:6.5px;color:#aaa;padding:3px 6px}
.f-submit{width:45px;height:12px;background:#333;color:var(--white);font-size:7px;display:flex;align-items:center;justify-content:center;border-radius:1px}
.social{display:flex;gap:4px}
.social i{width:12px;height:12px;border-radius:2px}
.badges{display:flex;gap:8px}
.badges i{height:16px;border-radius:3px;background:#d7d7d7}
.bottom{left:56px;top:1172px;width:645px;height:28px;background:var(--bar-bg);color:var(--white);font-size:7px;display:flex;align-items:center;padding-left:10px}
.cards{position:absolute;right:10px;top:7px;display:flex;gap:4px}
.cards i{width:26px;height:15px;background:#e9e9e9;border-radius:2px}
</style>
</head>
<body>

<header>
  <div class="abs brand"><span class="brand-mark"></span><span class="brand-name">parcelnook.com.au</span></div>
  <div class="abs brand-tag">gift basket &amp; hamper network</div>
  <div class="abs locale">En⌄ $⌄</div>
  <div class="abs account"><span>Create an account</span><span>Login</span></div>
  <div class="abs checkout">Checkout</div>
  <div class="abs cart">
    <svg width="10" height="9" viewBox="0 0 10 9"><path d="M0 1h2l1.5 5h5l1-3.5H3" fill="none" stroke="#333" stroke-width="1.2"/><circle cx="4" cy="8" r="1" fill="#333"/><circle cx="8" cy="8" r="1" fill="#333"/></svg>
    0 item(s) - $0.00 <span style="margin-left:auto;margin-right:7px;color:#666">⌄</span>
  </div>
</header>

<nav class="abs nav">
  <svg width="16" height="14" viewBox="0 0 16 14" style="margin-right:2px"><path d="M8 1L1 7h2v6h4V9h2v4h4V7h2z" fill="#fff"/></svg>
  <a>Easter</a><a class="drop">Mothers Day</a><a class="drop">Birthday</a><a class="drop">Anniversary</a><a>Romance</a><a>New Baby</a><a>Childrens</a><a>For Him</a><a>For Her</a>
</nav>

<section class="abs banner">
  <div class="abs" role="img" aria-label="Easter scene with daffodils, grass and painted eggs" style="left:300px;top:0;width:345px;height:180px;background:linear-gradient(160deg,#f3d24c 0%,#8fc24f 45%,#6fa63a 70%,#e79ab8 100%);opacity:.85"></div>
  <div class="abs banner-kicker">Join The 2014</div>
  <div class="abs banner-title">Easter<br>Egg hunts</div>
  <div class="abs dots"><i></i><i></i><i></i></div>
</section>

<aside>
  <div class="abs side-head" style="top:344px">Shop by basket price</div>
  <ul class="abs side-list" style="top:372px">
    <li class="on">Server Racks / Network Cabinets</li><li>Cable Management</li><li>Patch Leads</li><li>Cable Labels</li>
  </ul>
  <div class="abs side-head" style="top:458px">Shop by basket Style</div>
  <ul class="abs side-list" style="top:486px">
    <li class="on">Server Racks / Network Cabinets</li><li>Cable Management</li><li>Patch Leads</li><li>Cable Labels</li>
    <li>Cable Management</li><li>Patch Leads</li><li>Cable Labels</li>
    <li>Cable Management</li><li>Patch Leads</li><li>Cable Labels</li>
  </ul>
  <div class="abs side-head" style="top:682px">Shop by Occasion</div>
  <ul class="abs side-list" style="top:712px">
    <li class="on">Server Racks / Network Cabinets</li><li>Cable Management</li><li>Patch Leads</li><li>Cable Labels</li>
    <li>Cable Management</li><li>Patch Leads</li><li>Cable Labels</li><li>Cable Management</li><li>Patch Leads</li>
  </ul>
</aside>

<main>
  <div class="abs prod-head">Todays Top products</div>

  <!-- row 1 -->
  <div class="abs card" style="left:228px;top:398px"><div class="photo" role="img" aria-label="Chocolate bouquet basket" style="background:radial-gradient(circle,#e8743a,#7b4aa8 70%,#fff 71%)"></div><svg class="ribbon" width="30" height="30"><path d="M0 20L20 0h10L0 30z" fill="#6b449b"/><text x="8" y="19" transform="rotate(-45 12 16)" font-size="6" fill="#fff" font-family="Open Sans">NEW</text></svg><div class="name">Tasty Treats Chocolate Box</div><div class="price">$62.00</div><div class="buy">Buy Now</div></div>
  <div class="abs card" style="left:353px;top:398px"><div class="photo" role="img" aria-label="Easter bunny gift bag" style="background:radial-gradient(circle,#6d9fd0,#b7a070 60%,#fff 71%)"></div><div class="name">Tasty Treats Chocolate Box</div><div class="price">$62.00</div><div class="buy">Buy Now</div></div>
  <div class="abs card" style="left:477px;top:398px"><div class="photo" role="img" aria-label="Wine gift box" style="background:radial-gradient(circle,#5a3b7a,#cfc0a8 60%,#fff 71%)"></div><svg class="ribbon" width="30" height="30"><path d="M0 20L20 0h10L0 30z" fill="#6b449b"/><text x="8" y="19" transform="rotate(-45 12 16)" font-size="6" fill="#fff" font-family="Open Sans">NEW</text></svg><div class="name">Tasty Treats Chocolate Box</div><div class="price">$62.00</div><div class="buy">Buy Now</div></div>
  <div class="abs card" style="left:601px;top:398px"><div class="photo" role="img" aria-label="Christmas hamper platter" style="background:radial-gradient(circle,#9e2a2a,#c9a45a 60%,#fff 71%)"></div><div class="name">Tasty Treats Chocolate Box</div><div class="price">$62.00</div><div class="buy">Buy Now</div></div>

  <!-- row 2 -->
  <div class="abs card" style="left:228px;top:554px"><div class="photo" role="img" aria-label="Wine crate hamper" style="background:radial-gradient(circle,#3d4a32,#c8b48f 60%,#fff 71%)"></div><svg class="ribbon" width="30" height="30"><path d="M0 20L20 0h10L0 30z" fill="#6b449b"/><text x="8" y="19" transform="rotate(-45 12 16)" font-size="6" fill="#fff" font-family="Open Sans">NEW</text></svg><div class="name">Tasty Treats Chocolate Box</div><div class="price">$62.00</div><div class="buy">Buy Now</div></div>
  <div class="abs card" style="left:353px;top:554px"><div class="photo" role="img" aria-label="Stacked gift boxes" style="background:radial-gradient(circle,#f0a54a,#f4ede2 60%,#fff 71%)"></div><div class="name">Tasty Treats Chocolate Box</div><div class="price">$62.00</div><div class="buy">Buy Now</div></div>
  <div class="abs card" style="left:477px;top:554px"><div class="photo" role="img" aria-label="Fruit basket" style="background:radial-gradient(circle,#e4622c,#7da04a 60%,#fff 71%)"></div><svg class="ribbon" width="30" height="30"><path d="M0 20L20 0h10L0 30z" fill="#6b449b"/><text x="8" y="19" transform="rotate(-45 12 16)" font-size="6" fill="#fff" font-family="Open Sans">NEW</text></svg><div class="name">Tasty Treats Chocolate Box</div><div class="price">$62.00</div><div class="buy">Buy Now</div></div>
  <div class="abs card" style="left:601px;top:554px"><div class="photo" role="img" aria-label="Wine and glasses gift bag" style="background:radial-gradient(circle,#3a2a22,#b89a78 60%,#fff 71%)"></div><div class="name">Tasty Treats Chocolate Box</div><div class="price">$62.00</div><div class="buy" style="top:124px">Buy Now</div></div>

  <!-- row 3 -->
  <div class="abs card" style="left:228px;top:710px"><div class="photo" role="img" aria-label="Baby gift basket" style="background:radial-gradient(circle,#f1b7c8,#f6e7a8 60%,#fff 71%)"></div><svg class="ribbon" width="30" height="30"><path d="M0 20L20 0h10L0 30z" fill="#6b449b"/><text x="8" y="19" transform="rotate(-45 12 16)" font-size="6" fill="#fff" font-family="Open Sans">NEW</text></svg><div class="name">Tasty Treats Chocolate Box</div><div class="price">$62.00</div><div class="buy">Buy Now</div></div>
  <div class="abs card" style="left:353px;top:710px"><div class="photo" role="img" aria-label="Easter bunny gift bag" style="background:radial-gradient(circle,#6d9fd0,#b7a070 60%,#fff 71%)"></div><svg class="ribbon" width="30" height="30"><path d="M0 20L20 0h10L0 30z" fill="#6b449b"/><text x="8" y="19" transform="rotate(-45 12 16)" font-size="6" fill="#fff" font-family="Open Sans">NEW</text></svg><div class="name">Tasty Treats Chocolate Box</div><div class="price">$62.00</div><div class="buy">Buy Now</div></div>
  <div class="abs card" style="left:477px;top:710px"><div class="photo" role="img" aria-label="Easter chick egg basket" style="background:radial-gradient(circle,#f5df55,#f3e6b0 60%,#fff 71%)"></div><div class="name">Tasty Treats Chocolate Box</div><div class="price">$62.00</div><div class="buy">Buy Now</div></div>
  <div class="abs card" style="left:601px;top:710px"><div class="photo" role="img" aria-label="Easter egg gift pot" style="background:radial-gradient(circle,#f4f0e6,#6b7fd0 60%,#fff 71%)"></div><div class="name">Tasty Treats Chocolate Box</div><div class="price">$62.00</div><div class="buy">Buy Now</div></div>
</main>

<section class="abs seo">
  <div class="seo-col">
    <h2>Gift Baskets &amp; Hampers Delivered Throughout Australia</h2>
    <p>Browse Victorian Delivery areas including Gifts to Melbourne<br>Find Queensland Delivery locations and Gifts to Brisbane<br>Explore New South Wales Delivery areas with Gifts to Sydney<br>Discover Tasmanian Delivery locations including Gifts to Hobart</p>
  </div>
  <div class="seo-col">
    <h2>More Australian Gift Basket &amp; Hamper Delivery Locations</h2>
    <p>Find South Australian Delivery suburbs and Gifts to Adelaide<br>Browse ACT Delivery suburbs and Gifts to Canberra<br>Discover Northern Territory Delivery areas with Gifts to Darwin<br>Explore Western Australia Delivery suburbs plus Gifts to Perth</p>
  </div>
</section>

<footer>
  <div class="abs footer">
    <div class="abs" style="left:11px;top:18px">
      <div class="f-title">Contact Us</div>
      <ul class="f-list" style="margin-top:6px">
        <li>Web : http://www.parcelnook.com.au</li><li>Email : help@parcelnook.com.au</li><li>National : 1300 555 018</li><li>International : +61 1300 555 018</li>
      </ul>
      <div class="social" style="margin-top:10px"><i style="background:#c8283a"></i><i style="background:#3b5a99"></i><i style="background:#3aa3dd"></i><i style="background:#555"></i></div>
      <div class="badges" style="margin-top:10px"><i style="width:38px"></i><i style="width:38px"></i></div>
    </div>
    <div class="abs" style="left:184px;top:19px">
      <div class="f-title">Sitemap</div>
      <ul class="f-list" style="margin-top:6px"><li>Easter</li><li>Mothers Day</li><li>Get Well</li><li>Thank You</li><li>Birthday</li><li>Anniversary</li></ul>
    </div>
    <div class="abs" style="left:318px;top:19px">
      <div class="f-title">Sitemap</div>
      <ul class="f-list" style="margin-top:6px"><li>Romance</li><li>New Baby</li><li>Childrens</li><li>For Him</li><li>For Her</li></ul>
    </div>
    <div class="abs" style="left:440px;top:19px">
      <div class="f-title">Customer Feedback</div>
      <div class="f-input" style="margin-top:8px">Name</div>
      <div class="f-input" style="margin-top:6px">Email</div>
      <div class="f-input" style="margin-top:6px;height:37px">Message</div>
      <div class="f-submit" style="margin-top:6px">Submit</div>
    </div>
  </div>
  <div class="abs bottom">© 2014 Parcelnook&nbsp; | &nbsp;All Rights Reserved
    <div class="cards"><i></i><i></i><i></i></div>
  </div>
</footer>

</body>
</html>
```